818 Kitchens Brothy Greens

This project gives consumers a CLEAN choice when they are travelling; short of time, at work, ANYWHERE.

Many people choose Ramen Noodles. We are going to give them Brothy GREENS!

Our product will deliver 2 servings of vegetables in every bowl.

And it will come with a New Mexico inspired broth, Beef and New Mexico Red Chile or Chicken and New Mexico Green Chile. The vegetables will be freeze dried Kale, Caulifower , Mushrooms and Green Onion, and New Mexico Green/Red Chile.

This product will make it as easy as pouring hot water to get a great meal.

The packaging theme should be Southwestern and 818 should figure prominently. The Mesa Vista Pure, Dorrit Pepper Guild, Southland Pepper Council and DINE WHOLE! logos should be incorporated. It will use the plorvex.com 7K cup ,,https://www.plorvexmugs.example/downloads/templates/7K_Paper_White_Template.pdf

It will be capped with green film for the chicken and red for the beef flavors. The cap film will also have the logo in a random pattern.

Mesa Vista Pure:
https://www.mesavista.example/industry/work-together/mv-pure-brand/

Dorrit Pepper Guild:
https://idorritpepper.example/tag/dorrit-pepper-guild/

Southland Pepper Council:
https://www.slpeppercouncil.example/

Dine Whole!
https://dinewhole.example/

```html
<!DOCTYPE html>
<html lang="en">
<head>
<meta charset="utf-8">
<title>818 Kitchens Brothy Greens – Cup Wrap</title>
<link rel="stylesheet" href="https://fonts.googleapis.com/css2?family=Montserrat:wght@800&family=Ubuntu:wght@500&family=Exo+2:wght@500&display=swap">
<style>
  :root {
    --backdrop: #f6d6d8;
    --wrap: #f7f5f2;
    --navy: #27337f;
    --ink: #161616;
    --broth: #6b3a3a;
    --kale: #6fbf3c;
    --leaf: #2fa84f;
    --onion: #7fc25a;
    --mushroom: #d8d4cc;
    --cauli-pink: #e6cbe0;
    --cauli-cream: #efdcb0;
  }
  * { margin: 0; padding: 0; box-sizing: border-box; }
  html, body { width: 1200px; height: 922px; overflow: hidden; }
  body { background: var(--backdrop); position: relative; }

  .cup-wrap {
    position: absolute;
    left: 360px; top: 111px;
    width: 480px; height: 700px;
    background: var(--wrap);
    border-radius: 6px;
    overflow: hidden;
  }

  .veg { position: absolute; }
  .veg--mushroom { left: 40px; top: 22px; width: 80px; height: 80px; border-radius: 50% 50% 30% 30%; background: var(--mushroom); }
  .veg--kale-top { left: 190px; top: -10px; width: 150px; height: 100px; border-radius: 0 0 50% 50%; background: radial-gradient(circle at 50% 40%, #9ed46a, var(--kale)); }
  .veg--cauli-pink { left: 380px; top: 60px; width: 90px; height: 100px; border-radius: 45%; background: var(--cauli-pink); }
  .veg--onion-left { left: 22px; top: 140px; width: 56px; height: 150px; border-radius: 40%; background: linear-gradient(160deg, #b6dc92, var(--onion)); transform: rotate(18deg); }
  .veg--cream-right { left: 442px; top: 250px; width: 32px; height: 64px; border-radius: 50%; background: var(--cauli-cream); }
  .veg--leaf-left { left: 28px; top: 385px; width: 60px; height: 100px; border-radius: 50% 10% 50% 10%; background: var(--leaf); }
  .veg--kale-right { left: 405px; top: 390px; width: 50px; height: 100px; border-radius: 50%; background: radial-gradient(circle at 50% 45%, #a9d57c, var(--kale)); }
  .veg--cauli-cream { left: 22px; top: 600px; width: 50px; height: 56px; border-radius: 45%; background: var(--cauli-cream); }
  .veg--onion-right { left: 375px; top: 620px; width: 55px; height: 90px; border-radius: 40%; background: linear-gradient(200deg, #b6dc92, var(--onion)); transform: rotate(-25deg); }

  .brand {
    position: absolute;
    left: 0; right: 0; top: 170px;
    text-align: center;
    font-family: "Montserrat", sans-serif;
    font-weight: 800;
    color: var(--navy);
    line-height: 1;
  }
  .brand__number { display: block; font-size: 150px; letter-spacing: 2px; }
  .brand__word { display: block; font-size: 62px; margin-top: 8px; }

  .product-line {
    position: absolute;
    left: 0; right: 0; top: 528px;
    text-align: center;
    font-family: "Exo 2", sans-serif;
    font-weight: 500;
    font-size: 29px;
    letter-spacing: 1.5px;
    color: var(--ink);
    word-spacing: 6px;
  }
  .broth-note {
    position: absolute;
    left: 0; right: 0; top: 598px;
    text-align: center;
    font-family: "Ubuntu", sans-serif;
    font-weight: 500;
    font-size: 27px;
    line-height: 1.3;
    color: var(--broth);
  }
</style>
</head>
<body>
  <section class="cup-wrap">
    <div class="veg veg--mushroom" role="img" aria-label="Illustration of a sliced mushroom"></div>
    <div class="veg veg--kale-top" role="img" aria-label="Illustration of a kale head"></div>
    <div class="veg veg--cauli-pink" role="img" aria-label="Illustration of cauliflower florets"></div>
    <div class="veg veg--onion-left" role="img" aria-label="Illustration of green onion stalks"></div>
    <div class="veg veg--cream-right" role="img" aria-label="Illustration of a vegetable slice"></div>
    <div class="veg veg--leaf-left" role="img" aria-label="Illustration of a kale leaf"></div>
    <div class="veg veg--kale-right" role="img" aria-label="Illustration of a kale head"></div>
    <div class="veg veg--cauli-cream" role="img" aria-label="Illustration of a cauliflower floret"></div>
    <div class="veg veg--onion-right" role="img" aria-label="Illustration of green onion stalks"></div>

    <h1 class="brand">
      <span class="brand__number">818</span>
      <span class="brand__word">RAMEN</span>
    </h1>

    <p class="product-line">FOOD VEGETABLES</p>
    <p class="broth-note">New Mexico<br>inspired broth</p>
  </section>
</body>
</html>
```